VORTAL Business Card Design

We need a business card for a new company based on the Gold Coast, we are a new supplement distributing company called VORTAL Sports Nutrition - Bold Horizon Sports Nutrition. We are providing new science based bodybuilding and fitness supplementation. Our company has a key focus towards next generation. We are wanting a card that is cool, innovative and fresh. We would like to see the implementation of the below image in a fresh and very innovative design that stands out. The final design should communicate New, Innovative, Cool, Science and researched based.
Target Market(s)
The target market is fitness and bodybuilder enthusiasts. Young audience so very cool looking.
Industry/Entity Type
Fitness
Contact Information for Business Card
(front of card)
VORTAL Sports Nutrition.
Liam Darrow
CEO/Sport Nutrition Specialist
0472 638 904
Liam@vortalsportsfuel.example
www.vortalsportsfuel.example
(back of card)
Scientifically formulated supplement range
Private Nutrition consultations
comprehensive sports nutrition seminars
Requirements
Nice to have
- The card could have a cut out on one of the sides or one of the corners rounded off so the card looks different from a normal business card.
Should not have
- The colours need to complement each other and pop out.

```html
<!DOCTYPE html>
<html lang="en">
<head>
<meta charset="utf-8">
<title>VORTAL Sports Nutrition – Business Card</title>
<link rel="stylesheet" href="https://fonts.googleapis.com/css2?family=Noto+Sans:wght@700;800&family=Lato:ital,wght@0,300;1,300;1,400&display=swap">
<style>
  :root {
    --page-bg: #ffffff;
    --frame-navy: #0f2b3e;
    --card-blue: #1b7cc6;
    --card-steel: #8f9aa6;
    --card-grey: #b3bac2;
    --panel-white: rgba(255, 255, 255, 0.6);
    --ink-dark: #17344a;
    --ink-mid: #1e3447;
    --text-white: #ffffff;
    --badge-top: #0f3442;
    --badge-bottom: #040709;
    --badge-rim: #1d3a5c;
    --badge-mat: #dfe7f2;
    --accent-cyan: #5cc8f2;
  }
  html, body {
    margin: 0;
    padding: 0;
    overflow: hidden;
    background: var(--page-bg);
  }
  .card {
    position: relative;
    width: 1200px;
    height: 742px;
    overflow: hidden;
  }
  .card-shapes {
    position: absolute;
    inset: 0;
  }
  .brand-title {
    position: absolute;
    left: 543px;
    top: 168px;
    margin: 0;
    font: 800 41px/1 "Noto Sans", sans-serif;
    color: var(--text-white);
    letter-spacing: 0.5px;
    white-space: nowrap;
  }
  .contact {
    position: absolute;
    left: 543px;
    top: 0;
    margin: 0;
    color: var(--ink-mid);
    white-space: nowrap;
  }
  .contact-name {
    top: 283px;
    font: 700 39px/1 "Noto Sans", sans-serif;
    color: var(--ink-dark);
  }
  .contact-role {
    top: 337px;
    font: italic 300 35px/1 "Lato", sans-serif;
  }
  .contact-phone {
    top: 444px;
    font: 300 38px/1 "Lato", sans-serif;
  }
  .contact-email {
    top: 497px;
    font: 300 38px/1 "Lato", sans-serif;
  }
  .website {
    position: absolute;
    left: 129px;
    width: 1039px;
    top: 614px;
    margin: 0;
    text-align: center;
    font: 800 41px/1 "Noto Sans", sans-serif;
    color: var(--ink-dark);
    letter-spacing: 0.3px;
  }
  .badge {
    position: absolute;
    left: 27px;
    top: 172px;
    width: 441px;
    height: 393px;
    display: flex;
    flex-direction: column;
    align-items: center;
    justify-content: flex-end;
    padding-bottom: 40px;
    box-sizing: border-box;
  }
  .badge-name {
    margin: 0 0 46px;
    font: 800 64px/1 "Noto Sans", sans-serif;
    color: var(--text-white);
    letter-spacing: 3px;
  }
  .badge-tagline {
    margin: 0;
    font: italic 400 20px/1 "Lato", sans-serif;
    color: var(--text-white);
    letter-spacing: 0.3px;
  }
</style>
</head>
<body>
<main class="card">
  <svg class="card-shapes" width="1200" height="742" viewBox="0 0 1200 742" aria-hidden="true">
    <defs>
      <linearGradient id="card-face" x1="0" y1="0" x2="1" y2="0">
        <stop offset="0" stop-color="var(--card-blue)"/>
        <stop offset="0.45" stop-color="#6f9ccc"/>
        <stop offset="1" stop-color="var(--card-steel)"/>
      </linearGradient>
      <linearGradient id="lower-band" x1="0" y1="0" x2="1" y2="0">
        <stop offset="0" stop-color="#2a86cc"/>
        <stop offset="0.5" stop-color="#a9b8cc"/>
        <stop offset="1" stop-color="var(--card-grey)"/>
      </linearGradient>
      <linearGradient id="info-panel" x1="0" y1="0" x2="1" y2="0">
        <stop offset="0" stop-color="#ffffff" stop-opacity="0.25"/>
        <stop offset="0.35" stop-color="#ffffff" stop-opacity="0.7"/>
        <stop offset="1" stop-color="#ffffff" stop-opacity="0.6"/>
      </linearGradient>
      <linearGradient id="badge-fill" x1="0" y1="0" x2="0" y2="1">
        <stop offset="0" stop-color="var(--badge-top)"/>
        <stop offset="1" stop-color="var(--badge-bottom)"/>
      </linearGradient>
      <radialGradient id="light-glow" cx="0.55" cy="0.45" r="0.5">
        <stop offset="0" stop-color="#ffffff" stop-opacity="0.35"/>
        <stop offset="1" stop-color="#ffffff" stop-opacity="0"/>
      </radialGradient>
    </defs>

    <rect class="outer-frame" x="95" y="0" width="1105" height="742" rx="78" fill="var(--frame-navy)"/>
    <rect class="card-face" x="129" y="32" width="1039" height="656" rx="52" fill="url(#card-face)" stroke="#ffffff" stroke-width="4"/>
    <path class="card-lower-band" d="M131 590 H1166 V636 a50 50 0 0 1 -50 50 H181 a50 50 0 0 1 -50 -50 Z" fill="url(#lower-band)" opacity="0.85"/>
    <rect class="card-glow" role="img" aria-label="Soft light burst background" x="300" y="40" width="700" height="640" fill="url(#light-glow)"/>
    <rect class="info-panel" x="474" y="145" width="690" height="441" rx="26" fill="url(#info-panel)"/>

    <rect class="badge-mat" x="2" y="143" width="498" height="448" rx="42" fill="var(--badge-mat)" fill-opacity="0.9" stroke="var(--badge-rim)" stroke-width="3"/>
    <rect class="badge-plate" x="27" y="172" width="441" height="393" fill="url(#badge-fill)"/>
    <circle class="badge-dot" cx="247" cy="300" r="34" fill="var(--accent-cyan)"/>
  </svg>

  <div class="badge">
    <p class="badge-name">VORTAL</p>
    <p class="badge-tagline">BOLD HORIZON SPORTS NUTRITION.</p>
  </div>

  <h1 class="brand-title">VORTAL Sports Nutrition</h1>
  <p class="contact contact-name">Liam Darrow</p>
  <p class="contact contact-role">CEO/Sport Nutrition Specialist</p>
  <p class="contact contact-phone">0472 638 904</p>
  <p class="contact contact-email">Liam@vortalsportsfuel.example</p>
  <p class="website">www.vortalsportsfuel.example</p>
</main>
</body>
</html>
```